Marigold Premium Business Card Design Project

About the company: Here at Fernhaven Botanics, we focus on cosmetic products that based on essential oils and different kinds of plant essences. All of our raw materials are pure organic and specially selected from local producers in Australia.

I'm here to look for a unique business card design, to replace the current one later on, so I don't have many requirements. Why I wanna restrict designers' creativity?

All I know is: 1. do not make it too complicated, straight forward, simple and pure. 2. this design may be used for other purposes (i.e. logo and slogan on the front, Brand Story and contact details at the back). Therefor, I'd like to have the design for 3 layouts, one only have logo, slogan, contact detials, one for the brand story, the other one for the personal business card with staff's mob etc...

A vector graphic is required, i.e. eps, ai, easy for me to resize.

Round Corner.

Thanks

Plz add "Hand made in Australia" in the design, cheers.

Target Market(s)

Women aged yr 20-50

Industry/Entity Type

Business

Requirements
Must have
• Logo: please see attacment (eps, ai)

Slogan: Moonlit Velvet Glow

Website:www.fernhavenbotanics.com.au

Address: temporary not available

Phone: temporary not available

"Hand made in Australia"

Nice to have
• Prefer round corner

```html
<!DOCTYPE html>
<html lang="en">
<head>
<meta charset="utf-8">
<title>Fernhaven Botanics – Business Cards</title>
<link rel="stylesheet" href="https://fonts.googleapis.com/css2?family=Dancing+Script:wght@500&family=Questrial&display=swap">
<style>
  :root {
    --stage: #e9e6e7;
    --card-front: #f6c3cf;
    --card-back: #ffffff;
    --pattern-pink: #fbe3e9;
    --band-pink: #f6c9d4;
    --rose-light: #f4a3b6;
    --rose-deep: #d8375f;
    --brand: #d23a62;
    --ink: #3a3a3a;
    --link: #cc1f3c;
  }
  * { box-sizing: border-box; margin: 0; padding: 0; }
  html, body { width: 1200px; height: 900px; overflow: hidden; background: var(--stage); }
  .canvas { position: relative; width: 1200px; height: 900px; }

  .card {
    position: absolute;
    width: 560px;
    height: 330px;
    border-radius: 26px;
    overflow: hidden;
    box-shadow: 0 6px 18px rgba(0,0,0,.18);
  }
  .card__pattern { position: absolute; inset: 0; }

  /* Front */
  .card--front { left: 80px; top: 80px; background: var(--card-front); }
  .card--front .card__pattern { background: radial-gradient(circle at 50% 45%, #f8ccd7 0%, var(--card-front) 70%); }
  .brand {
    position: absolute; left: 0; right: 0; top: 96px;
    display: flex; align-items: center; justify-content: center; gap: 14px;
  }
  .brand__dot { width: 16px; height: 16px; border-radius: 50%; background: var(--brand); }
  .brand__name {
    font-family: "Dancing Script", cursive; font-weight: 500;
    font-size: 62px; color: var(--brand); line-height: 1;
  }
  .slogan {
    position: absolute; left: 0; right: 0; top: 250px; text-align: center;
    font-family: "Dancing Script", cursive; font-weight: 500;
    font-size: 28px; color: var(--brand);
  }

  /* Back */
  .card--back { left: 560px; top: 480px; background: var(--card-back); }
  .card--back .card__pattern { background: linear-gradient(135deg, #ffffff 0%, var(--pattern-pink) 100%); }
  .rose {
    position: absolute; right: 48px; top: 10px; width: 150px; height: 150px;
    border-radius: 50%;
    background: radial-gradient(circle at 45% 50%, #fde6ec 0%, var(--rose-light) 40%, var(--rose-deep) 100%);
  }
  .person {
    position: absolute; left: 0; top: 112px; width: 250px; height: 66px;
    background: var(--band-pink); padding: 8px 0 0 24px;
    font-family: "Questrial", sans-serif; color: var(--ink);
  }
  .person__name { font-size: 24px; line-height: 1.1; }
  .person__role { font-size: 16px; margin-top: 4px; }
  .contact {
    position: absolute; left: 24px; top: 200px;
    font-family: "Questrial", sans-serif; font-size: 14px; color: var(--ink);
    list-style: none;
  }
  .contact li { display: flex; align-items: center; gap: 8px; line-height: 20px; }
  .contact svg { width: 11px; height: 11px; fill: var(--ink); flex: none; }
  .contact__web { color: var(--link); font-weight: bold; }
  .address {
    position: absolute; left: 24px; top: 272px;
    font-family: "Questrial", sans-serif; font-size: 14px; line-height: 20px; color: var(--ink);
    font-style: normal;
  }
  .made-in {
    position: absolute; right: 28px; bottom: 30px;
    font-family: "Dancing Script", cursive; font-weight: 500;
    font-size: 26px; color: var(--ink);
  }
</style>
</head>
<body>
<main class="canvas">

  <section class="card card--front" aria-label="Card front">
    <div class="card__pattern" role="img" aria-label="Soft pink leaf pattern background"></div>
    <div class="brand">
      <span class="brand__dot"></span>
      <span class="brand__name">Fernhaven Botanics</span>
    </div>
    <p class="slogan">Moonlit Velvet Glow</p>
  </section>

  <section class="card card--back" aria-label="Card back">
    <div class="card__pattern" role="img" aria-label="Faint pink leaf pattern background"></div>
    <div class="rose" role="img" aria-label="Illustration of a pink rose"></div>
    <div class="person">
      <p class="person__name">Clara Westbrook</p>
      <p class="person__role">Manager</p>
    </div>
    <ul class="contact">
      <li>
        <svg viewBox="0 0 24 24" aria-hidden="true"><path d="M6.6 10.8a15 15 0 0 0 6.6 6.6l2.2-2.2a1 1 0 0 1 1-.25 11.4 11.4 0 0 0 3.6.57 1 1 0 0 1 1 1V20a1 1 0 0 1-1 1A17 17 0 0 1 3 4a1 1 0 0 1 1-1h3.5a1 1 0 0 1 1 1c0 1.25.2 2.45.57 3.57a1 1 0 0 1-.25 1z"/></svg>
        +61 3 9555 0147
      </li>
      <li>
        <svg viewBox="0 0 24 24" aria-hidden="true"><path d="M2 5h20v14H2z M2 5l10 8 10-8" /></svg>
        hello@fernhavenbotanics.com.au
      </li>
      <li class="contact__web">
        <svg viewBox="0 0 24 24" aria-hidden="true"><circle cx="12" cy="12" r="10"/></svg>
        www.fernhavenbotanics.com.au
      </li>
    </ul>
    <address class="address">12 Wattle Lane,<br>Daylesford, VIC 3460</address>
    <p class="made-in">Hand made in Australia</p>
  </section>

</main>
</body>
</html>
```